Quick Banner Ad Job for IT Services Company

Need a collection of banner ads based around a common theme and message.

Main Theme.

IT Support and Managed Services - IT support you can rely on.
Free remote monitoring and alerting*
*conditions apply <-- this in small text

Secondary Content

Our customers are attracted by our exceptional level of customer service and trust us in providing them with support and advice over a long term relationship.

Note:
* Logos and colours attached. Only use these colours.
* Font is to be Myriad Pro

* Delivery will require the following sizes.
Leaderboard: 728×90
Medium Rectangle: 300×250
Wide Skyscraper: 160×600

Do the initial draft in leaderboard, other sizes can be worked once we have an agreed design for the main

Final delivery will also need to be in an editable format, not just final images.

Industry/Entity Type

It Company

```html
<!DOCTYPE html>
<html lang="en">
<head>
<meta charset="UTF-8">
<title>IT Support Leaderboard Banner</title>
<link href="https://fonts.googleapis.com/css2?family=Source+Sans+3:wght@400;600;700&display=swap" rel="stylesheet">
<style>
  :root {
    --navy: #0a3350;
    --sky: #1ab4e8;
    --blue: #0a7cc4;
    --ink: #111111;
    --muted: #7a7a7a;
    --frame: #d2d2d2;
    --bg-top: #ffffff;
    --bg-bottom: #e2e3e5;
  }
  * { margin: 0; padding: 0; box-sizing: border-box; }
  html, body {
    width: 1200px;
    height: 1000px;
    overflow: hidden;
    background: #ffffff;
    font-family: "Source Sans 3", sans-serif;
  }
  .leaderboard {
    position: absolute;
    left: 235px;
    top: 79px;
    width: 730px;
    height: 92px;
    border: 1px solid var(--frame);
    background: linear-gradient(to bottom, var(--bg-top) 0%, var(--bg-top) 55%, var(--bg-bottom) 100%);
  }
  .brand {
    position: absolute;
    left: 12px;
    top: 20px;
    display: flex;
    align-items: center;
    gap: 14px;
  }
  .brand-mark {
    width: 56px;
    height: 56px;
    border-radius: 50%;
    background: var(--blue);
  }
  .brand-name {
    font-weight: 700;
    font-size: 38px;
    letter-spacing: -0.5px;
    color: var(--navy);
    line-height: 1;
  }
  .message {
    position: absolute;
    left: 230px;
    top: 8px;
    width: 495px;
    text-align: center;
  }
  .headline {
    font-weight: 700;
    font-size: 16px;
    color: var(--navy);
    line-height: 19px;
    letter-spacing: -0.1px;
  }
  .offer {
    font-weight: 700;
    font-size: 16px;
    color: var(--sky);
    line-height: 18px;
  }
  .body-copy {
    font-weight: 400;
    font-size: 12px;
    color: var(--ink);
    line-height: 15px;
    margin-top: 1px;
  }
  .conditions {
    font-weight: 600;
    font-size: 9.5px;
    color: var(--muted);
    line-height: 12px;
  }
</style>
</head>
<body>
  <div class="leaderboard">
    <div class="brand">
      <div class="brand-mark"></div>
      <span class="brand-name">CoreLink</span>
    </div>
    <div class="message">
      <p class="headline">IT SUPPORT AND MANAGED SERVICES - IT SUPPORT YOU CAN RELY ON.</p>
      <p class="offer">Free Remote Monitoring And Alerting*</p>
      <p class="body-copy">Our customers are attracted by our exceptional level of customer service and trust us<br>in providing them with support and advice over a long term relationship.</p>
      <p class="conditions">*conditions apply</p>
    </div>
  </div>
</body>
</html>
```